Brellow Gateworks garage door installation service and repairs

I need a business card design for my company that is called Brellow Gateworks, I install, service, repair and automate garaged doors.
I want my card to look simple and neat but I also want the information such as contact number, email address and website to be clear and noticeable. I would love a simple logo if possible, I would like to see the color blue in the card but not overpowering.

Industry/Entity Type

Garage

```html
<!DOCTYPE html>
<html lang="en">
<head>
<meta charset="UTF-8">
<title>Brellow Gateworks – Business Card</title>
<link rel="stylesheet" href="https://fonts.googleapis.com/css2?family=Raleway:wght@300;700&display=swap">
<style>
  :root {
    --page-bg: #eeeae4;
    --card-blue: #33b4e6;
    --card-white: #ffffff;
    --mark-ink: #2e2e2e;
    --card-shadow: rgba(40, 30, 20, 0.22);
  }
  * { margin: 0; padding: 0; box-sizing: border-box; }
  html, body {
    width: 1200px;
    height: 800px;
    overflow: hidden;
    background: var(--page-bg);
  }
  .canvas {
    position: relative;
    width: 1200px;
    height: 800px;
    display: flex;
    align-items: center;
    justify-content: center;
  }
  .business-card {
    position: relative;
    width: 900px;
    height: 514px;
    background: var(--card-blue);
    border-radius: 22px;
    box-shadow: 0 14px 36px var(--card-shadow);
    display: flex;
    align-items: center;
    font-family: "Raleway", sans-serif;
  }
  .brand-seal {
    position: absolute;
    left: 70px;
    top: 50%;
    transform: translateY(-50%);
    width: 250px;
    height: 250px;
    border-radius: 50%;
    background: var(--card-white);
    display: flex;
    align-items: center;
    justify-content: center;
    text-align: center;
  }
  .brand-name {
    font-family: "Raleway", sans-serif;
    font-weight: 700;
    color: var(--mark-ink);
    font-size: 29px;
    line-height: 1.15;
    letter-spacing: 1px;
    text-transform: uppercase;
  }
  .contact-list {
    position: absolute;
    left: 440px;
    top: 50%;
    transform: translateY(-58%);
    list-style: none;
  }
  .contact-item {
    display: flex;
    align-items: center;
    gap: 18px;
    color: var(--card-white);
    font-weight: 300;
    font-size: 30px;
    letter-spacing: 0.5px;
    height: 52px;
  }
  .contact-icon {
    width: 30px;
    height: 30px;
    flex: none;
  }
</style>
</head>
<body>
<main class="canvas">
  <section class="business-card" aria-label="Brellow Gateworks business card">
    <div class="brand-seal">
      <span class="brand-name">Brellow<br>Gateworks</span>
    </div>
    <ul class="contact-list">
      <li class="contact-item">
        <svg class="contact-icon" viewBox="0 0 30 30" aria-hidden="true">
          <circle cx="15" cy="15" r="14" fill="#fff"/>
          <rect x="7.5" y="9.5" width="15" height="11" rx="1" fill="none" stroke="#33b4e6" stroke-width="1.8"/>
          <path d="M7.8 10 L15 16 L22.2 10" fill="none" stroke="#33b4e6" stroke-width="1.8"/>
        </svg>
        <span>email@email.com</span>
      </li>
      <li class="contact-item">
        <svg class="contact-icon" viewBox="0 0 30 30" aria-hidden="true">
          <circle cx="15" cy="15" r="14" fill="#fff"/>
          <circle cx="15" cy="15" r="8" fill="none" stroke="#33b4e6" stroke-width="1.6"/>
          <ellipse cx="15" cy="15" rx="3.5" ry="8" fill="none" stroke="#33b4e6" stroke-width="1.4"/>
          <path d="M7 15 H23 M8.5 11 H21.5 M8.5 19 H21.5" stroke="#33b4e6" stroke-width="1.4"/>
        </svg>
        <span>website.com</span>
      </li>
      <li class="contact-item">
        <svg class="contact-icon" viewBox="0 0 30 30" aria-hidden="true">
          <circle cx="15" cy="15" r="13" fill="none" stroke="#fff" stroke-width="2"/>
          <path d="M11 8.5 C9 9.5 8.5 12 10.5 15.5 C12.5 19 15.5 21.5 18.5 21.5 C20 21.5 21 20.5 21.3 19.5 L18.8 17.3 L17 18.5 C15.3 17.7 13.6 15.8 12.6 13.8 L13.8 12 Z" fill="#fff"/>
        </svg>
        <span>0123456789</span>
      </li>
    </ul>
  </section>
</main>
</body>
</html>
```